HCA Twirl under our moonbeams

My nonprofit social service agency is having a fun gala based on the TV show twirl under moonbeams, and we need the key design for an invitation. The event is a dinner and will have 7 local well-known people dance in a contest-like setting with a nationally known host. This does not need to be the final invitation (RSVP, list of dancers/hosts, etc.). All I need at this point is a great design for the cover to give this event an identity and entice people to attend and/or donate to the cause! Though our logo colors are blue/green/burgandy, this can use black/gold/silver/white as well. Our website is www.hcalorvin.org if that helps explain who we are.

Also, it can be abstract. And it does not have to include ballroom dancers if the word mark or other graphics are eye catching.

Target Market(s)

Donors, upscale, higher income,45-70, men and women (though women will more likely make the decision to attend)

Industry/Entity Type

Tv

Requirements
Must have
• The wording to be incorporated into the invitation cover is:
Harborview Community Aid
Celebrates Stepping Up for Decades with
Twirl Under Moonbeams
hosted by Host Name (will give the final name when confirmed)

Saturday, November 8, 2014
7 pm
Marlowe Cincinnati Crestwood Tower
Nice to have
• I'd like to see something other than ballroom dancers just to give my committee some options. Is it possible to show footprints of dancers (man's shoe with woman's high heels) as the design element? Something that can be used across the invite (rsvp card).
Should not have
• You have free range to create and have fun! If you use our logo colors, either choose one color as the focus, or just be sure to focus on green and burgandy together

```html
<!DOCTYPE html>
<html lang="en">
<head>
<meta charset="utf-8">
<title>Harborview Community Aid – Twirl Under Moonbeams</title>
<link href="https://fonts.googleapis.com/css2?family=Great+Vibes&family=Arimo:wght@400&display=swap" rel="stylesheet">
<style>
  :root {
    --stage: #000000;
    --card: #ffffff;
    --ink: #111111;
    --blue: #1a66cc;
    --burgundy: #9b2f66;
    --green: #3a9a3a;
    --shoe-light: #d9d9d9;
    --shoe-dark: #8a8a8a;
    --string: #555555;
  }
  * { margin: 0; padding: 0; box-sizing: border-box; }
  html, body { width: 1200px; height: 900px; overflow: hidden; background: var(--stage); }
  .canvas { position: relative; width: 1200px; height: 900px; background: var(--stage); }
  .invitation {
    position: absolute; left: 319px; top: 48px; width: 564px; height: 805px;
    background: var(--card); overflow: hidden;
    font-family: "Arimo", Arial, sans-serif; color: var(--ink);
  }
  .brand {
    position: absolute; left: 0; right: 0; top: 50px;
    display: flex; align-items: center; justify-content: center; gap: 10px;
    font-size: 24px; color: var(--burgundy);
  }
  .brand-dot { width: 22px; height: 22px; border-radius: 50%; background: var(--green); }
  .tagline {
    position: absolute; left: 0; right: 0; top: 101px; text-align: center; font-size: 16px;
  }
  .event-title { font-weight: 400; }
  .title-script { font-family: "Great Vibes", cursive; font-weight: 400; line-height: 1; white-space: nowrap; }
  .title-twirl {
    position: absolute; left: 30px; top: 140px; font-size: 130px; color: var(--blue);
  }
  .title-line-two {
    position: absolute; right: 24px; top: 250px;
    display: flex; align-items: baseline; gap: 10px; white-space: nowrap;
  }
  .title-joiner { font-family: "Arimo", Arial, sans-serif; font-weight: 400; font-size: 28px; color: var(--burgundy); }
  .title-moonbeams { font-size: 72px; color: var(--green); }
  .strings { position: absolute; left: 0; top: 0; width: 564px; height: 805px; }
  .shoe { position: absolute; border-radius: 6px; }
  .shoe-boot {
    left: 164px; top: 440px; width: 127px; height: 160px;
    background: linear-gradient(160deg, var(--shoe-light), var(--shoe-dark));
  }
  .shoe-heel {
    left: 323px; top: 530px; width: 95px; height: 140px;
    background: linear-gradient(160deg, var(--shoe-light), var(--shoe-dark));
  }
  .host { position: absolute; left: 38px; top: 618px; }
  .host-label { font-size: 26px; }
  .host-name { font-size: 22px; margin-top: 6px; letter-spacing: 1px; }
  .details { position: absolute; left: 0; top: 704px; list-style: none; }
  .details li { display: flex; align-items: center; height: 24px; font-size: 19px; }
  .details .swatch { width: 30px; height: 19px; margin-right: 8px; }
  .swatch-blue { background: var(--blue); }
  .swatch-burgundy { background: var(--burgundy); }
  .swatch-green { background: var(--green); }
</style>
</head>
<body>
<div class="canvas">
  <section class="invitation">
    <div class="brand"><span class="brand-dot"></span><span class="brand-name">Harborview Community Aid</span></div>
    <p class="tagline">Celebrates Stepping Up for Decades</p>

    <h1 class="event-title">
      <span class="title-script title-twirl">Twirl</span>
      <span class="title-line-two">
        <span class="title-joiner">under our</span>
        <span class="title-script title-moonbeams">Moonbeams</span>
      </span>
    </h1>

    <svg class="strings" viewBox="0 0 564 805" aria-hidden="true">
      <path d="M208 290 C240 320 180 340 215 370 C250 400 190 415 222 440" fill="none" stroke="var(--string)" stroke-width="1.5"/>
      <path d="M412 350 C380 385 420 410 380 440 C340 470 410 490 370 515 C360 522 364 526 366 530" fill="none" stroke="var(--string)" stroke-width="1.5"/>
    </svg>

    <div class="shoe shoe-boot" role="img" aria-label="Sketch of a man's dance boot hanging from a string"></div>
    <div class="shoe shoe-heel" role="img" aria-label="Sketch of a woman's high-heeled shoe hanging from a string"></div>

    <div class="host">
      <p class="host-label">hosted by</p>
      <p class="host-name">XXXXX XXXXXX</p>
    </div>

    <ul class="details">
      <li><span class="swatch swatch-blue"></span>Saturday, November 8, 2014</li>
      <li><span class="swatch swatch-burgundy"></span>7 pm</li>
      <li><span class="swatch swatch-green"></span>Marlowe Cincinnati Crestwood Tower</li>
    </ul>
  </section>
</div>
</body>
</html>
```